Business Card and Letterhead Design for Public Accounting Firm

Business card and letterhead design for a CPA Firm located in Orange County, CA. We're looking for a modern and professional design utilizing our existing logo. We'd like a clean "less is more" look, but also something that catches the eye. We provide a high level of service to our clients. Open to single or double sided business cards.

Additional info: color numbers on logo
Blue :
R 0
G 83
B 125

#00537D

Silver :

R 154
G 154
B 154

#9A9A9A

Target Market(s)

Businesses and individuals

Industry/Entity Type

Accounting

Contact Information for Business Card

Moss Whitfield & Danby LLP - 4827 Larkspur Vale Road, Irvine, CA 92614 - (949)731-2864 - mwdaccts.example

Font styles to use
Serif
Sans Serif
Other font styles liked:
• See font file uploaded

Colors
0054AA
0677BA
7BADD7
CADEEF
E8F1F8

Requirements
Nice to have
• Possibly use the font file provided which matches our logo, but adjust to be not in all caps

```html
<!DOCTYPE html>
<html lang="en">
<head>
<meta charset="utf-8">
<title>Moss Whitfield &amp; Danby LLP — Business Card</title>
<link rel="stylesheet" href="https://fonts.googleapis.com/css2?family=EB+Garamond:wght@400;500&display=swap">
<style>
  :root {
    --canvas: #d7d7d7;
    --brand-blue: #00537d;
    --silver: #9a9a9a;
    --paper: #f1f1ef;
    --white: #ffffff;
  }
  * { box-sizing: border-box; margin: 0; padding: 0; }
  html, body {
    width: 1200px;
    height: 1051px;
    overflow: hidden;
    background: var(--canvas);
    font-family: "EB Garamond", Georgia, serif;
  }
  .card-set {
    position: absolute;
    inset: 0;
    display: flex;
    align-items: center;
    justify-content: center;
    gap: 40px;
  }
  .card {
    position: relative;
    width: 520px;
    height: 297px;
    box-shadow: 0 10px 30px rgba(0,0,0,0.12);
  }
  .card--front { background: var(--paper); }
  .card--back { background: var(--brand-blue); }

  .firm-name {
    position: absolute;
    left: 0;
    right: 0;
    text-align: center;
    font-weight: 500;
    font-size: 25px;
    letter-spacing: 3px;
    text-transform: uppercase;
    line-height: 1.25;
  }
  .card--front .firm-name { top: 62px; color: var(--brand-blue); }
  .card--back .firm-name { top: 112px; color: var(--white); }

  .contact {
    position: absolute;
    left: 0;
    right: 0;
    top: 186px;
    display: flex;
    justify-content: center;
    align-items: center;
    color: var(--silver);
    font-size: 15px;
    line-height: 1.35;
  }
  .contact__address { text-align: right; padding-right: 18px; }
  .contact__divider {
    width: 1px;
    height: 48px;
    background: var(--silver);
    opacity: 0.7;
  }
  .contact__lines { padding-left: 18px; }
  .contact__line { display: flex; align-items: center; gap: 6px; }
  .contact__icon { width: 11px; height: 11px; flex: none; }
</style>
</head>
<body>
  <main class="card-set">
    <section class="card card--front" aria-label="Business card front">
      <h1 class="firm-name">Moss Whitfield<br>&amp; Danby LLP</h1>
      <div class="contact">
        <address class="contact__address" style="font-style:normal">
          4827 Larkspur Vale Road<br>Irvine, CA 92614
        </address>
        <span class="contact__divider"></span>
        <div class="contact__lines">
          <p class="contact__line">
            <svg class="contact__icon" viewBox="0 0 24 24" aria-hidden="true"><path fill="var(--brand-blue)" d="M6.6 10.8a15.1 15.1 0 0 0 6.6 6.6l2.2-2.2a1 1 0 0 1 1-.25 11.4 11.4 0 0 0 3.6.57 1 1 0 0 1 1 1V20a1 1 0 0 1-1 1A17 17 0 0 1 3 4a1 1 0 0 1 1-1h3.5a1 1 0 0 1 1 1c0 1.25.2 2.45.57 3.57a1 1 0 0 1-.25 1z"/></svg>
            (949) 731-2864
          </p>
          <p class="contact__line">
            <svg class="contact__icon" viewBox="0 0 24 24" aria-hidden="true"><circle cx="12" cy="12" r="10" fill="none" stroke="var(--brand-blue)" stroke-width="2.4"/><path d="M2 12h20M12 2c3 3 3 17 0 20M12 2c-3 3-3 17 0 20" fill="none" stroke="var(--brand-blue)" stroke-width="2"/></svg>
            mwdaccts.example
          </p>
        </div>
      </div>
    </section>
    <section class="card card--back" aria-label="Business card back">
      <h2 class="firm-name">Moss Whitfield<br>&amp; Danby LLP</h2>
    </section>
  </main>
</body>
</html>
```